Vantor Medica Innovative Business Card

Stunning business card. Background will be black. Letters in gold. Modern yet simple design that is attention grabbing. QR code leading to site. Attractive primarily to males ages 30 to 50 but also to females in same age range looking for beauty and mental health products

Target Market(s)

Males in the 30-50 age demographics

Industry/Entity Type

Pharmaceuticals selling erectile dysfunction and mens health medications

Contact Information for Business Card

www.vantormedica.example; (775) BUY-KELO; info@vantormedica.example

Colors
FFC000
F8CF3A
FAE287
FDF2CF
FEFAEE

Requirements
Must have
• Black business card with gold letters.
Nice to have
• perhaps just the logo or the "R" icon by itself on one side
Should not have
• too much content so it does not look busy

```html
<!DOCTYPE html>
<html lang="en">
<head>
<meta charset="UTF-8">
<title>Vantor Medica – Business Card</title>
<link href="https://fonts.googleapis.com/css2?family=Montserrat:wght@400;500;700;800&display=swap" rel="stylesheet">
<style>
  :root {
    --page: #1c1c1e;
    --card-dark: #221e1f;
    --card-mid: #3a3435;
    --gold: #e2bf4a;
    --gold-light: #f2d877;
    --gold-deep: #c9a032;
    --gold-shade: #8a6d26;
    --text-light: #e8e4e2;
  }
  * { margin: 0; padding: 0; box-sizing: border-box; }
  html, body { width: 1200px; height: 1200px; overflow: hidden; background: var(--page); }
  body { font-family: "Montserrat", sans-serif; }
  .sheet {
    width: 1200px; height: 1200px;
    display: flex; flex-direction: column; align-items: center; justify-content: center; gap: 60px;
  }
  .card {
    position: relative; width: 840px; height: 480px; overflow: hidden;
    background: radial-gradient(ellipse at 55% 30%, var(--card-mid) 0%, var(--card-dark) 70%);
    box-shadow: 0 12px 30px rgba(0,0,0,.5);
  }

  /* Back side */
  .card-back .pattern-field {
    position: absolute; inset: 0;
    background: linear-gradient(135deg, #2e292a 0%, #1f1b1c 55%, #2a2526 100%);
  }
  .card-back .corner-mark {
    position: absolute; left: 120px; top: 60px;
    width: 44px; height: 44px; border-radius: 50%; background: var(--gold);
  }
  .card-back .brand-name {
    position: absolute; right: 120px; bottom: 110px;
    font-weight: 800; font-size: 62px; letter-spacing: 1px; color: var(--gold);
  }

  /* Front side */
  .brand-lockup {
    position: absolute; left: 0; right: 0; top: 118px;
    display: flex; align-items: center; justify-content: center; gap: 18px;
  }
  .brand-lockup .brand-dot { width: 60px; height: 60px; border-radius: 50%; background: var(--gold); }
  .brand-lockup .brand-name { font-weight: 800; font-size: 52px; color: var(--gold); letter-spacing: 1px; }

  .contact-list {
    position: absolute; left: 60px; top: 205px; list-style: none;
    display: flex; flex-direction: column; gap: 12px;
  }
  .contact-list li {
    display: flex; align-items: center; gap: 12px;
    font-size: 22px; font-weight: 400; color: var(--text-light);
  }
  .contact-list svg { width: 20px; height: 20px; flex: none; }

  .holder {
    position: absolute; right: 60px; top: 300px; text-align: right;
  }
  .holder .holder-name { font-weight: 700; font-size: 38px; color: var(--gold); }
  .holder .holder-role { font-weight: 400; font-size: 26px; color: var(--text-light); margin-top: 4px; }

  .gold-band { position: absolute; left: 0; bottom: 0; width: 840px; height: 110px; }
</style>
</head>
<body>
<main class="sheet">

  <section class="card card-back" aria-label="Card back">
    <div class="pattern-field" role="img" aria-label="Repeating embossed brand symbol pattern in dark grey"></div>
    <span class="corner-mark"></span>
    <div class="brand-name">VANTOR MEDICA</div>
  </section>

  <section class="card card-front" aria-label="Card front">
    <div class="brand-lockup">
      <span class="brand-dot"></span>
      <span class="brand-name">VANTOR MEDICA</span>
    </div>

    <ul class="contact-list">
      <li>
        <svg viewBox="0 0 24 24" fill="var(--gold)"><path d="M6.6 10.8a15.1 15.1 0 0 0 6.6 6.6l2.2-2.2a1 1 0 0 1 1-.25 11.4 11.4 0 0 0 3.6.57 1 1 0 0 1 1 1V20a1 1 0 0 1-1 1A17 17 0 0 1 3 4a1 1 0 0 1 1-1h3.5a1 1 0 0 1 1 1c0 1.25.2 2.45.57 3.6a1 1 0 0 1-.25 1z"/></svg>
        (775)-410-226
      </li>
      <li>
        <svg viewBox="0 0 24 24" fill="var(--gold)"><path d="M3 5h18v14H3z" fill="none" stroke="var(--gold)" stroke-width="2"/><path d="M3 5l9 8 9-8" fill="none" stroke="var(--gold)" stroke-width="2"/></svg>
        info@vantormedica.example
      </li>
      <li>
        <svg viewBox="0 0 24 24" fill="none" stroke="var(--gold)" stroke-width="2"><circle cx="12" cy="12" r="9"/><path d="M3 12h18M12 3c3 3 3 15 0 18M12 3c-3 3-3 15 0 18"/></svg>
        www.vantormedica.example
      </li>
    </ul>

    <div class="holder">
      <div class="holder-name">Dorian Vale</div>
      <div class="holder-role">Founder &amp; Director</div>
    </div>

    <svg class="gold-band" viewBox="0 0 840 110" preserveAspectRatio="none" aria-hidden="true">
      <defs>
        <linearGradient id="bandGold" x1="0" y1="0" x2="1" y2="0">
          <stop offset="0" stop-color="var(--gold-light)"/>
          <stop offset="1" stop-color="var(--gold-deep)"/>
        </linearGradient>
      </defs>
      <path d="M0 38 H360 C380 38 385 45 395 50 L0 50 Z" fill="var(--gold-shade)"/>
      <path d="M0 62 H370 C400 62 405 20 440 20 H840 V110 H0 Z" fill="url(#bandGold)"/>
    </svg>
  </section>

</main>
</body>
</html>
```